Logo and Business Card for Dental Office

We are opening a periodontal office (dental specialist for dental implants and gum diseases). It is a brand new state of the art facility with a focus on the most effective treatments for retaining natural teeth, or replacing teeth with implants when they must be lost. Strong emphasis on customer service and amenities for patient comfort. We are located just outside of Boston, MA.

Target Market(s)

potential adult patients, dentists in the community that will refer patients for specialized care

Industry/Entity Type

Dental

Requirements
Must have
• business name, address, phone number, website
Marcus T. Pellinger, DMD LLC
427 Corliss Street, Ste 305
Wayland, MA 01694
508-555-0172
508-555-0148 Fax
DrPellinger.example

the uploaded file has a rough version of what I'm looking for in the logo, I like the colors but it can be varies some.
Nice to have
• simple logo or symbol on business card, one possible idea I had was an abstract symbol of a screw or threads that might represent a dental implant, the attached file gives an idea of where to start.
Should not have
• I want a professional feel, no cartoons of teeth that appear childish, etc
The font should be easy to read with no curly/swirly shapes.

```html
<!DOCTYPE html>
<html lang="en">
<head>
<meta charset="utf-8">
<title>Marcus T. Pellinger, DMD LLC — Logo and Business Card</title>
<link rel="stylesheet" href="https://fonts.googleapis.com/css2?family=Quicksand:wght@600&family=Crimson+Text&family=Questrial&family=Open+Sans:wght@600&display=swap">
<style>
  :root {
    --brand-red: #a3242a;
    --ink-dark: #3a3a3a;
    --ink-soft: #6b6b6b;
    --card-dark: #333333;
    --card-light: #ffffff;
    --card-edge: #cfcfcf;
    --page: #ffffff;
  }
  * { margin: 0; padding: 0; box-sizing: border-box; }
  html, body { width: 1200px; height: 788px; overflow: hidden; background: var(--page); }
  .canvas { position: relative; width: 1200px; height: 788px; }

  .mark-circle { position: absolute; border-radius: 50%; border: 5px solid var(--brand-red); }

  /* logo lockup */
  .lockup .mark-circle { left: 70px; top: 96px; width: 100px; height: 100px; }
  .lockup-title {
    position: absolute; left: 196px; top: 100px;
    font-family: "Quicksand", sans-serif; font-weight: 600;
    font-size: 36px; line-height: 52px; color: var(--brand-red);
  }
  .lockup-name {
    position: absolute; left: 199px; top: 211px;
    font-family: "Crimson Text", serif; font-size: 20px; color: var(--ink-dark);
  }

  /* card back */
  .card-back {
    position: absolute; left: 564px; top: 78px; width: 568px; height: 349px;
    background: var(--card-dark);
  }
  .card-back .mark-circle { left: 234px; top: 80px; width: 100px; height: 100px; }
  .card-back-web {
    position: absolute; left: 212px; top: 226px; white-space: nowrap;
    font-family: "Open Sans", sans-serif; font-weight: 600; font-size: 22px;
    line-height: 30px; color: var(--card-light);
  }

  /* card front */
  .card-front {
    position: absolute; left: 188px; top: 345px; width: 570px; height: 349px;
    background: var(--card-light); border: 1px solid var(--card-edge);
  }
  .card-front .mark-circle { left: 38px; top: 54px; width: 64px; height: 64px; border-width: 4px; }
  .card-front-name {
    position: absolute; left: 129px; top: 75px;
    font-family: "Crimson Text", serif; font-size: 21px; color: var(--ink-dark);
  }
  .card-front-details {
    position: absolute; left: 130px;
    font-family: "Questrial", sans-serif; font-size: 15px; line-height: 20px;
    color: var(--ink-soft); list-style: none;
  }
  .contact { top: 186px; }
  .address { top: 258px; }
</style>
</head>
<body>
<main class="canvas">
  <section class="lockup">
    <div class="mark-circle" aria-hidden="true"></div>
    <h1 class="lockup-title">Periodontics<br>&amp; Dental Implants</h1>
    <p class="lockup-name">Marcus T. Pellinger, DMD LLC</p>
  </section>

  <section class="card-back">
    <div class="mark-circle" aria-hidden="true"></div>
    <p class="card-back-web">DrPellinger.example</p>
  </section>

  <section class="card-front">
    <div class="mark-circle" aria-hidden="true"></div>
    <p class="card-front-name">Marcus T. Pellinger, DMD LLC</p>
    <ul class="card-front-details contact">
      <li>123 456 7890</li>
      <li>yourname@example.com</li>
    </ul>
    <ul class="card-front-details address">
      <li>address address address</li>
      <li>address address address</li>
    </ul>
  </section>
</main>
</body>
</html>
```